Our business name is Kelvobrin. The project we want this business card to feature is our project & c

We need a business card design for our companies project 'Marquelent'. We would like our companies logo to feature (company is named Kelvobrin) as well as our companies project (Marquelent). The Marquelent is split up into different websites that all interact with each other's content.

On the front of the card we would like a brief intro of what our project is about with the project logo. Somewhere like it to be clear each part of the Marquelent interacts with each other, and we encourage users to create and share their projects.

On the back we would like a example of some of the parts of the Marquelent with their logos and explanation of what they are about.
On either the front/ back would need contact details/website details/ social networking details.

Under the logo we'd like our slogan: 'Content. Projects. Activity. Always on its way at the Marquelent'. Somewhere should have project name 'Marquelent'.

Industry/Entity Type

Business

Contact Information for Business Card

A modern looking design, that includes all key details. Should include company name 'Kelvobrin' and company project name larger: 'Marquelent'

Font styles to use
Sans Serif

Requirements
Must have
• Phone number
• Contact email
• Space for social icons

```html
<!DOCTYPE html>
<html lang="en">
<head>
<meta charset="utf-8">
<title>Marquelent business card</title>
<link rel="stylesheet" href="https://fonts.googleapis.com/css2?family=Arimo:wght@400;700&display=swap">
<style>
  :root {
    --page: #e7e4df;
    --card: #050505;
    --card-sheen: #262626;
    --white: #f4f4f4;
    --orange: #e8882a;
    --rule: #7a7a7a;
    --dot-blue: #c4c9e6;
    --dot-yellow: #eeee80;
  }
  * { box-sizing: border-box; margin: 0; padding: 0; }
  html, body {
    width: 1200px; height: 913px; overflow: hidden;
    background: var(--page);
    font-family: "Arimo", Arial, sans-serif;
  }
  .stage {
    position: relative; width: 1200px; height: 913px;
    display: flex; align-items: center; justify-content: center; gap: 50px;
  }
  .card {
    position: relative; width: 525px; height: 300px;
    background: linear-gradient(135deg, var(--card) 0%, var(--card) 45%, var(--card-sheen) 60%, var(--card) 78%);
    box-shadow: 0 12px 30px rgba(0,0,0,.25);
    overflow: hidden;
  }

  /* front: name block */
  .brand { position: absolute; left: 40px; top: 30px; }
  .brand__company {
    font-weight: 700; font-size: 17px; letter-spacing: 1.5px;
    color: var(--white); text-transform: uppercase; padding-left: 52px;
  }
  .brand__project {
    font-weight: 700; font-size: 40px; letter-spacing: 2px;
    color: var(--orange); text-transform: uppercase;
    line-height: 1.05; margin-top: 4px;
  }
  .brand__slogan {
    font-weight: 400; font-size: 14px; letter-spacing: 1.4px;
    color: var(--white); text-transform: uppercase; margin-top: 4px;
    padding-left: 22px;
  }

  .person { position: absolute; right: 312px; top: 168px; text-align: right; }
  .person__name { font-size: 20px; color: var(--white); }
  .person__role { font-size: 13px; color: var(--orange); margin-top: 2px; }

  .divider-v {
    position: absolute; left: 228px; top: 156px; width: 1px; height: 64px;
    background: linear-gradient(var(--card), var(--orange), var(--card));
  }

  .contacts { position: absolute; left: 244px; top: 160px; list-style: none; }
  .contacts li {
    display: flex; align-items: center; gap: 8px;
    font-size: 12.5px; color: var(--white); height: 18px;
  }
  .contacts svg { width: 11px; height: 11px; fill: var(--orange); flex: none; }

  .divider-h {
    position: absolute; left: 22px; right: 22px; top: 236px; height: 1px;
    background: linear-gradient(90deg, transparent, var(--rule) 20%, var(--rule) 80%, transparent);
  }

  .socials {
    position: absolute; left: 22px; right: 22px; top: 248px;
    display: flex; justify-content: space-between; list-style: none;
  }
  .socials li {
    display: flex; flex-direction: column; align-items: center; gap: 5px;
    font-size: 13px; color: var(--white); width: 78px;
  }
  .socials .marker { width: 12px; height: 12px; background: var(--orange); border-radius: 2px; }

  /* back: part marks */
  .part-mark { position: absolute; width: 80px; height: 56px; border-radius: 50%; }
  .part-mark--blue { left: 185px; top: 72px; background: var(--dot-blue); }
  .part-mark--yellow { left: 268px; top: 148px; background: var(--dot-yellow); }
</style>
</head>
<body>
<main class="stage">
  <section class="card card--front" aria-label="Card front">
    <div class="brand">
      <p class="brand__company">Kelvobrin</p>
      <p class="brand__project">Marquelent</p>
      <p class="brand__slogan">Content. Projects. Activity</p>
    </div>

    <div class="person">
      <p class="person__name">Dara Voss</p>
      <p class="person__role">CEO</p>
    </div>

    <div class="divider-v"></div>

    <ul class="contacts">
      <li>
        <svg viewBox="0 0 24 24" aria-hidden="true"><path d="M6.6 10.8a15 15 0 0 0 6.6 6.6l2.2-2.2c.3-.3.7-.4 1-.2 1.1.4 2.3.6 3.6.6.6 0 1 .4 1 1V20c0 .6-.4 1-1 1A17 17 0 0 1 3 4c0-.6.4-1 1-1h3.5c.6 0 1 .4 1 1 0 1.3.2 2.5.6 3.6.1.3 0 .7-.2 1z"/></svg>
        000.000.0000
      </li>
      <li>
        <svg viewBox="0 0 24 24" aria-hidden="true"><path d="M2 5h20v14H2z M2 5l10 8 10-8" stroke="#050505" stroke-width="1.5"/></svg>
        username@webaddress.com
      </li>
      <li>
        <svg viewBox="0 0 24 24" aria-hidden="true"><circle cx="12" cy="12" r="10"/><path d="M2 12h20M12 2c3 3 3 17 0 20M12 2c-3 3-3 17 0 20" stroke="#050505" stroke-width="1.4" fill="none"/></svg>
        www.webaddress.com
      </li>
    </ul>

    <div class="divider-h"></div>

    <ul class="socials">
      <li><span class="marker"></span>username</li>
      <li><span class="marker"></span>username</li>
      <li><span class="marker"></span>username</li>
      <li><span class="marker"></span>username</li>
      <li><span class="marker"></span>username</li>
      <li><span class="marker"></span>username</li>
    </ul>
  </section>

  <section class="card card--back" aria-label="Card back">
    <span class="part-mark part-mark--blue" role="img" aria-label="Mark of a Marquelent part"></span>
    <span class="part-mark part-mark--yellow" role="img" aria-label="Mark of a Marquelent part"></span>
  </section>
</main>
</body>
</html>
```